8x8 Social Media Ad - Harbor Summit Expo

Attention Real Estate Agents
Please join us for our
Quarterly Real Estate Training Expo
The 2nd Saturday of February, May, August and November
Our Next Training Expo is _________________________________
From 9 am to 1 pm
at
Marlowe Suites Fernridge Station
4187 Copperleaf Lane, Greenbelt, MD 20770
Scheduled Speakers
9:00 am - Desmond Pryce - Orientation
9:30 am - Terrell Oakes - Multiple Income Streams / Keystone Track
10:00 am - Lorna Beckett - Marketing though Social Media
10:45 am - Raul Denning - Generating Business through Kelp-Nest
11:30 am - Tunde Adesemi - Real Estate Investing
12:15 pm - Marcus Oyelowo - (Main Speaker) Training Topic TBA
For more information call Desmond Pryce at (240) 555-0192 or email dpryce@harborsummithomes.example

```html
<!DOCTYPE html>
<html lang="en">
<head>
<meta charset="utf-8">
<title>Harbor Summit Expo – Quarterly Real Estate Training Expo</title>
<link rel="stylesheet" href="https://fonts.googleapis.com/css2?family=Poppins:wght@400;500;600;700;800&family=Kalam:wght@400&display=swap">
<style>
  :root {
    --teal: #2190a0;
    --teal-band: #2391a3;
    --ink: #111111;
    --black: #0b0b0b;
    --white: #ffffff;
    --photo-a: #3b4f72;
    --photo-b: #5b6070;
  }
  * { box-sizing: border-box; margin: 0; padding: 0; }
  html, body { width: 1200px; height: 1200px; overflow: hidden; background: var(--white); }
  .ad {
    position: relative; width: 1200px; height: 1200px;
    background: var(--white); font-family: "Poppins", sans-serif; color: var(--ink);
  }
  .brand {
    position: absolute; top: 70px; left: 0; width: 100%;
    display: flex; justify-content: center; align-items: center; gap: 14px;
  }
  .brand-mark { width: 34px; height: 34px; background: var(--teal); }
  .brand-name { font-weight: 700; font-size: 34px; color: var(--teal); letter-spacing: 0.5px; }
  .intro {
    position: absolute; top: 188px; width: 100%; text-align: center;
    font-family: "Kalam", cursive; font-size: 46px; color: var(--ink);
  }
  .title {
    position: absolute; top: 258px; width: 100%; text-align: center;
    font-weight: 700; font-size: 45px; color: var(--teal); letter-spacing: -0.3px;
  }
  .schedule-pill {
    position: absolute; top: 321px; left: 182px; width: 836px; height: 51px;
    background: var(--teal); border-radius: 26px; color: var(--white);
    display: flex; align-items: center; justify-content: center;
    font-size: 23px; font-weight: 500;
  }
  .schedule-pill strong { font-weight: 800; margin-left: 6px; letter-spacing: -0.4px; }
  .hours {
    position: absolute; top: 378px; width: 100%; text-align: center;
    font-weight: 700; font-size: 46px; letter-spacing: -0.5px;
  }
  .hours .accent { color: var(--teal); }
  .venue {
    position: absolute; top: 436px; left: 312px; display: flex; gap: 16px; align-items: flex-start;
  }
  .venue svg { margin-top: 6px; }
  .venue p { font-size: 21px; font-weight: 500; line-height: 28px; }
  .teal-band { position: absolute; top: 653px; left: 0; width: 100%; height: 392px; background: var(--teal-band); }
  .speaker-photos { position: absolute; top: 511px; left: 59px; display: flex; gap: 23px; }
  .speaker-photo {
    width: 161px; height: 250px; border: 4px solid var(--white);
    border-radius: 0 64px 0 64px;
    background: linear-gradient(160deg, var(--photo-b), var(--photo-a));
    box-shadow: 0 6px 12px rgba(0,0,0,0.3);
  }
  .speaker-photo.outdoor { background: linear-gradient(170deg, #5d8a4c, #3e6a96); }
  .speaker-photo.warm { background: linear-gradient(170deg, #9aa3a3, #b56a50); }
  .speaker-photo.light { background: linear-gradient(170deg, #c9c9c9, #35445e); }
  .speaker-table {
    position: absolute; top: 797px; left: 70px; width: 1060px; height: 228px;
    border: 2px solid var(--white); display: grid;
    grid-template-columns: 189px 139px 199px 1fr; color: var(--white);
  }
  .speaker-table > div { border-right: 2px solid var(--white); }
  .speaker-table > div:last-child { border-right: none; }
  .table-label {
    display: flex; flex-direction: column; align-items: center; justify-content: center;
    font-weight: 700; font-size: 23px; line-height: 30px; text-align: center; padding-top: 10px;
  }
  .table-label svg { margin-bottom: 10px; }
  .table-col { padding: 12px 0 0 26px; font-size: 18.5px; line-height: 33.4px; }
  .table-col.names { padding-left: 24px; }
  .table-col.topics { padding-left: 25px; }
  .footer { position: absolute; top: 1045px; left: 0; width: 100%; height: 155px; background: var(--black); color: var(--white); }
  .contact-line { position: absolute; top: 18px; left: 0; width: 100%; text-align: center; white-space: nowrap; }
  .contact-line .script { font-family: "Kalam", cursive; font-size: 34px; }
  .contact-line .name { font-weight: 700; font-size: 35px; margin-left: 10px; }
  .contact-row { position: absolute; top: 82px; left: 180px; display: flex; align-items: center; }
  .contact-item { display: flex; align-items: center; gap: 16px; }
  .contact-item .icon {
    width: 44px; height: 44px; border-radius: 50%; background: var(--teal);
    display: flex; align-items: center; justify-content: center;
  }
  .phone { font-weight: 700; font-size: 30px; }
  .email { font-size: 25px; margin-left: 0; }
  .contact-item + .contact-item { margin-left: 60px; }
</style>
</head>
<body>
<main class="ad">
  <header class="brand">
    <span class="brand-mark"></span>
    <span class="brand-name">Harbor Summit Realty Group</span>
  </header>

  <p class="intro">Please join us for our</p>
  <h1 class="title">Quarterly Real Estate Training Expo</h1>
  <div class="schedule-pill">The 2nd Saturday of <strong>February, May, August and November</strong></div>
  <p class="hours">FROM <span class="accent">9 AM</span> TO <span class="accent">1 PM</span></p>

  <div class="venue">
    <svg width="30" height="42" viewBox="0 0 30 42" aria-hidden="true">
      <path d="M15 1C7.3 1 1 7.2 1 14.9 1 25 15 41 15 41s14-16 14-26.1C29 7.2 22.7 1 15 1z" fill="var(--teal)"/>
      <circle cx="15" cy="15" r="6" fill="var(--white)"/>
    </svg>
    <p>Marlowe Suites Fernridge Station<br>4187 Copperleaf Lane, Greenbelt, MD 20770</p>
  </div>

  <div class="teal-band"></div>

  <div class="speaker-photos">
    <div class="speaker-photo" role="img" aria-label="Portrait of Desmond Pryce"></div>
    <div class="speaker-photo light" role="img" aria-label="Portrait of Terrell Oakes"></div>
    <div class="speaker-photo" role="img" aria-label="Portrait of Lorna Beckett"></div>
    <div class="speaker-photo outdoor" role="img" aria-label="Portrait of Raul Denning"></div>
    <div class="speaker-photo light" role="img" aria-label="Portrait of Tunde Adesemi"></div>
    <div class="speaker-photo warm" role="img" aria-label="Portrait of Marcus Oyelowo"></div>
  </div>

  <section class="speaker-table">
    <div class="table-label">
      <svg width="62" height="62" viewBox="0 0 62 62" aria-hidden="true">
        <circle cx="31" cy="10" r="9" fill="var(--white)"/>
        <path d="M14 30c0-7 7-11 17-11s17 4 17 11v2H14z" fill="var(--white)"/>
        <path d="M2 34h58l-8 12H10z" fill="var(--white)"/>
        <rect x="16" y="46" width="30" height="16" fill="var(--white)"/>
        <rect x="22" y="36" width="18" height="3" fill="var(--teal-band)"/>
      </svg>
      SCHEDULED<br>SPEAKERS
    </div>
    <div class="table-col">9:00 am<br>9:30 am<br>10:00 am<br>10:45 am<br>11:30 am<br>12:15 pm</div>
    <div class="table-col names">Desmond Pryce<br>Terrell Oakes<br>Lorna Beckett<br>Raul Denning<br>Tunde Adesemi<br>Marcus Oyelowo</div>
    <div class="table-col topics">Orientation<br>Multiple Income Streams / Keystone Track<br>Marketing though Social Media<br>Generating Business through Kelp-Nest<br>Real Estate Investing<br>Marcus Oyelowo - (Main Speaker) Training Topic TBA</div>
  </section>

  <footer class="footer">
    <p class="contact-line"><span class="script">For more information Call :</span><span class="name">DESMOND PRYCE</span></p>
    <div class="contact-row">
      <div class="contact-item">
        <span class="icon">
          <svg width="24" height="24" viewBox="0 0 24 24" aria-hidden="true">
            <path d="M6.6 10.8c1.4 2.8 3.8 5.1 6.6 6.6l2.2-2.2c.3-.3.7-.4 1-.2 1.1.4 2.3.6 3.6.6.6 0 1 .4 1 1V20c0 .6-.4 1-1 1C10.6 21 3 13.4 3 4c0-.6.4-1 1-1h3.5c.6 0 1 .4 1 1 0 1.3.2 2.5.6 3.6.1.3 0 .7-.2 1z" fill="var(--white)"/>
          </svg>
        </span>
        <span class="phone">(240) 555-0192</span>
      </div>
      <div class="contact-item">
        <span class="icon">
          <svg width="24" height="24" viewBox="0 0 24 24" aria-hidden="true">
            <rect x="2" y="5" width="20" height="14" rx="2" fill="var(--white)"/>
            <path d="M3 6.5l9 6.5 9-6.5" fill="none" stroke="var(--teal)" stroke-width="1.8"/>
          </svg>
        </span>
        <span class="email">dpryce@harborsummithomes.example</span>
      </div>
    </div>
  </footer>
</main>
</body>
</html>
```